Poster design for a company operating care homes in the UK showcasing our core values

We need a poster to display in our care homes showcasing our new core values:

Purpose
We are driven by a clear understanding of why we do what we do: to enrich lives, honour legacies and make a meaningful difference every day, for our residents, their families, our colleagues and our community.

Excellence
We hold ourselves to the highest standards, delivering exceptional care and creating an environment where both residents and staff can thrive.

Openness
We build trust through honest, respectful communication, welcoming feedback, sharing ideas, and embracing change as a path to continuous growth.

Passion
We are passionate about delivering exceptional care. We take pride in what we do and in making a real difference in people’s lives.

Learning
We are committed to personal and professional growth; empowering each other through ongoing development, reflection, and shared knowledge.

Empathy
We actively listen and seek to understand before being understood, recognising the unique stories, feelings, and needs of others.

I have attached a small graphic that we would like you try to incorporate, in addition to our company logo. Please theme the rest of the poster around our company colours.

```html
<!DOCTYPE html>
<html lang="en">
<head>
<meta charset="utf-8">
<title>Halwell – Core Values</title>
<link rel="stylesheet" href="https://fonts.googleapis.com/css2?family=Fraunces:wght@500&family=Montserrat:wght@800&family=Raleway:wght@400;600&display=swap">
<style>
  :root {
    --blush: #f6dace;
    --navy: #38536f;
    --peach: #eea886;
    --taupe: #d5b6ad;
    --rim: #f4f1ef;
    --white: #ffffff;
  }
  html, body { margin: 0; padding: 0; overflow: hidden; background: var(--blush); }
  .poster { display: block; width: 948px; height: 1200px; background: var(--blush); }
  .brand-name { font-family: "Raleway", sans-serif; font-weight: 600; fill: var(--navy); }
  .poster-title { font-family: "Montserrat", sans-serif; font-weight: 800; fill: var(--navy); }
  .value-title { font-family: "Fraunces", serif; font-weight: 500; font-size: 29px; }
  .value-body { font-family: "Raleway", sans-serif; font-weight: 400; font-size: 14.3px; }
  .on-navy { fill: var(--peach); }
  .on-peach { fill: var(--navy); }
  .wedge-navy { fill: var(--navy); }
  .wedge-peach { fill: var(--peach); }
  .divider { fill: var(--taupe); stroke: var(--rim); stroke-width: 4; }
  .icon-line { fill: none; stroke-width: 3; stroke-linecap: round; stroke-linejoin: round; }
</style>
</head>
<body>
<svg class="poster" viewBox="0 0 948 1200" xmlns="http://www.w3.org/2000/svg">
  <defs>
    <linearGradient id="hub-ring" x1="0" y1="0" x2="1" y2="0">
      <stop offset="0" stop-color="#38536f"/>
      <stop offset="1" stop-color="#eea886"/>
    </linearGradient>
  </defs>

  <!-- Brand header -->
  <g class="brand">
    <circle cx="350" cy="57" r="17" fill="#38536f"/>
    <text class="brand-name" x="378" y="74" font-size="48" letter-spacing="1">HALWELL</text>
  </g>

  <text class="poster-title" x="153" y="203" font-size="92" textLength="644" lengthAdjust="spacingAndGlyphs">CORE VALUES</text>

  <!-- Values wheel -->
  <g class="wheel">
    <circle cx="474" cy="691" r="443" fill="var(--rim)"/>
    <path class="wedge-navy"  d="M474 691 L474 254 A437 437 0 0 0 95.5 472.5 Z"/>
    <path class="wedge-peach" d="M474 691 L852.5 472.5 A437 437 0 0 0 474 254 Z"/>
    <path class="wedge-navy"  d="M474 691 L852.5 909.5 A437 437 0 0 0 852.5 472.5 Z"/>
    <path class="wedge-peach" d="M474 691 L474 1128 A437 437 0 0 0 852.5 909.5 Z"/>
    <path class="wedge-navy"  d="M474 691 L95.5 909.5 A437 437 0 0 0 474 1128 Z"/>
    <path class="wedge-peach" d="M474 691 L95.5 472.5 A437 437 0 0 0 95.5 909.5 Z"/>

    <g class="dividers">
      <rect class="divider" x="458" y="240" width="32" height="902"/>
      <rect class="divider" x="458" y="240" width="32" height="902" transform="rotate(60 474 691)"/>
      <rect class="divider" x="458" y="240" width="32" height="902" transform="rotate(-60 474 691)"/>
    </g>

    <circle cx="474" cy="691" r="153" fill="url(#hub-ring)"/>
    <circle cx="474" cy="691" r="142" fill="var(--white)"/>
    <text class="brand-name" x="474" y="704" font-size="36" text-anchor="middle" letter-spacing="1">HALWELL</text>
  </g>

  <!-- Empathy -->
  <g class="value value-empathy">
    <rect role="img" aria-label="Outline icon of two heads facing each other beneath a heart" x="320" y="298" width="72" height="56" rx="10" fill="var(--peach)"/>
    <text class="value-title on-navy" x="390" y="383" text-anchor="middle">Empathy</text>
    <text class="value-body on-navy" text-anchor="end">
      <tspan x="428" y="408">We hold ourselves to the highest</tspan>
      <tspan x="428" y="425">standards, delivering exceptional</tspan>
      <tspan x="428" y="442">care and creating an environment where</tspan>
      <tspan x="428" y="459">both residents and staff can thrive.</tspan>
    </text>
  </g>

  <!-- Purpose -->
  <g class="value value-purpose">
    <g class="icon-target">
      <circle cx="566" cy="328" r="26" fill="var(--navy)"/>
      <circle cx="566" cy="328" r="19" fill="var(--peach)"/>
      <circle cx="566" cy="328" r="13" fill="var(--navy)"/>
      <circle cx="566" cy="328" r="7" fill="var(--peach)"/>
      <line class="icon-line" x1="566" y1="328" x2="600" y2="307" stroke="var(--navy)"/>
      <path d="M596 303 L604 300 L603 309 Z" fill="var(--navy)"/>
    </g>
    <text class="value-title on-peach" x="521" y="383">Purpose</text>
    <text class="value-body on-peach">
      <tspan x="521" y="408">We are driven by a clear understanding</tspan>
      <tspan x="521" y="425">of why we do what we do: to enrich lives,</tspan>
      <tspan x="521" y="442">honour legacies and make a meaningful</tspan>
      <tspan x="521" y="459">difference every day, for our residents,</tspan>
      <tspan x="521" y="476">their families, our colleagues and</tspan>
      <tspan x="521" y="493">our community.</tspan>
    </text>
  </g>

  <!-- Learning -->
  <g class="value value-learning">
    <g class="icon-book" stroke="var(--navy)">
      <path class="icon-line" d="M118 624 C108 618 97 616 90 618 L90 584 C97 581 108 583 118 590 Z"/>
      <path class="icon-line" d="M118 624 C128 618 139 616 146 618 L146 584 C139 581 128 583 118 590 Z"/>
      <path class="icon-line" d="M88 592 L88 626 C100 624 110 626 118 630 C126 626 136 624 148 626 L148 592"/>
      <line class="icon-line" x1="102" y1="603" x2="108" y2="606"/>
      <line class="icon-line" x1="128" y1="600" x2="136" y2="596"/>
      <line class="icon-line" x1="128" y1="606" x2="136" y2="602"/>
    </g>
    <text class="value-title on-peach" x="64" y="657">Learning</text>
    <text class="value-body on-peach">
      <tspan x="64" y="684">We are committed to personal and</tspan>
      <tspan x="64" y="701">professional growth;</tspan>
      <tspan x="64" y="718">empowering each other through</tspan>
      <tspan x="64" y="735">ongoing development, reflection,</tspan>
      <tspan x="64" y="752">and shared knowledge.</tspan>
    </text>
  </g>

  <!-- Excellence -->
  <g class="value value-excellence" stroke="var(--peach)">
    <g class="icon-award">
      <circle class="icon-line" cx="808" cy="595" r="15"/>
      <circle class="icon-line" cx="808" cy="595" r="9" stroke-width="2"/>
      <path d="M808 590 L809.6 593.6 L813.4 594 L810.5 596.5 L811.3 600.2 L808 598.3 L804.7 600.2 L805.5 596.5 L802.6 594 L806.4 593.6 Z" fill="var(--peach)" stroke="none"/>
      <path class="icon-line" d="M800 608 L793 625 L800 621 L803 628 L808 611"/>
      <path class="icon-line" d="M816 608 L823 625 L816 621 L813 628 L808 611"/>
    </g>
    <text class="value-title on-navy" x="867" y="657" text-anchor="end" stroke="none">Excellence</text>
    <text class="value-body on-navy" text-anchor="end" stroke="none">
      <tspan x="878" y="684">We hold ourselves to the highest</tspan>
      <tspan x="878" y="701">standards, delivering exceptional</tspan>
      <tspan x="878" y="718">care and creating an environment</tspan>
      <tspan x="878" y="735">where both residents and</tspan>
      <tspan x="878" y="752">staff can thrive.</tspan>
    </text>
  </g>

  <!-- Passion -->
  <g class="value value-passion">
    <rect role="img" aria-label="Silhouette of a person standing with arms spread wide" x="352" y="837" width="66" height="70" rx="8" fill="var(--peach)"/>
    <text class="value-title on-navy" x="428" y="926" text-anchor="end">Passion</text>
    <text class="value-body on-navy" text-anchor="end">
      <tspan x="428" y="954">We are passionate about</tspan>
      <tspan x="428" y="971">delivering exceptional care.</tspan>
      <tspan x="428" y="988">We take pride in what</tspan>
      <tspan x="428" y="1005">we do and in making a</tspan>
      <tspan x="428" y="1022">real difference in people’s lives.</tspan>
    </text>
  </g>

  <!-- Openness -->
  <g class="value value-openness">
    <rect role="img" aria-label="Silhouette of a head in profile with an open top" x="553" y="838" width="50" height="62" rx="10" fill="var(--navy)"/>
    <text class="value-title on-peach" x="522" y="926">Openness</text>
    <text class="value-body on-peach">
      <tspan x="523" y="954">We build trust through honest,</tspan>
      <tspan x="523" y="971">respectful communication,</tspan>
      <tspan x="523" y="988">welcoming feedback, sharing ideas,</tspan>
      <tspan x="523" y="1005">and embracing change as a path to</tspan>
      <tspan x="523" y="1022">continuous growth.</tspan>
    </text>
  </g>
</svg>
</body>
</html>
```